Modern Lawfirm Business Card Design

We're looking for a business card to incorporate the newly created logo we had made.

Ideally looking for a law firm business card demonstrating, modern, minimalist, strong/bold design.

I'm open to any design honestly, but nothing "flashy".

Target Market(s)

Immigration law, family immigration, humanitarian, general legal

Industry/Entity Type

Law Firm

Contact Information for Business Card

Please use dummy information, name, street address, city, state, phone number, email, website.

Font styles to use
Serif
Sans Serif

Requirements
Must have
• Please use dummy information, name, street address, city, state, phone number, email, website.

```html
<!DOCTYPE html>
<html lang="en">
<head>
<meta charset="utf-8">
<title>Calloway Immigration Law – Business Cards</title>
<link rel="stylesheet" href="https://fonts.googleapis.com/css2?family=Roboto:wght@400;700&display=swap">
<style>
  :root {
    --backdrop: #ececec;
    --card: #ffffff;
    --navy: #034a86;
    --sky: #0aa1de;
    --ink: #1b1b1b;
    --icon: #ffffff;
  }
  * { margin: 0; padding: 0; box-sizing: border-box; }
  html, body { width: 1200px; height: 799px; overflow: hidden; }
  body {
    background: var(--backdrop);
    font-family: "Roboto", Arial, sans-serif;
    position: relative;
  }
  .card {
    position: absolute;
    top: 250px;
    width: 525px;
    height: 300px;
    background: var(--card);
    box-shadow: 0 6px 18px rgba(0,0,0,0.12);
    overflow: hidden;
  }
  .card--details { left: 50px; }
  .card--front { left: 625px; }
  .card__bands { position: absolute; inset: 0; width: 100%; height: 100%; }
  .firm-name {
    position: absolute;
    color: var(--navy);
    font-weight: 700;
    font-size: 21px;
    line-height: 25px;
    letter-spacing: 0.4px;
    white-space: nowrap;
  }
  .card--front .firm-name {
    left: 272px; top: 150px;
    transform: translate(-50%, -50%);
    text-align: center;
  }
  .card--details .firm-name {
    left: 40px; top: 48px;
  }
  .contact {
    position: absolute;
    left: 290px; top: 168px;
    color: var(--ink);
    font-size: 12px;
    line-height: 18px;
  }
  .contact__name { font-weight: 700; }
  .contact__role { font-weight: 400; }
  .icon { fill: none; stroke: var(--icon); stroke-width: 1.3; stroke-linejoin: round; stroke-linecap: round; }
  .icon--solid { fill: var(--icon); stroke: none; }
</style>
</head>
<body>

  <section class="card card--details" aria-label="Card side with contact details">
    <svg class="card__bands" viewBox="0 0 525 300" aria-hidden="true">
      <polyline points="302,0 302,118 262,158 262,300" fill="none" stroke="var(--navy)" stroke-width="18"/>
      <!-- person -->
      <g transform="translate(262,177)">
        <circle class="icon--solid" cx="0" cy="-2.5" r="2.5"/>
        <path class="icon--solid" d="M-5 5 a5 4.5 0 0 1 10 0 z"/>
      </g>
      <!-- phone -->
      <g transform="translate(262,195)">
        <path class="icon--solid" d="M-4.5 -5 h3 l1 3 -1.8 1.3 q1 2.2 3 3 l1.3 -1.8 3 1 v3 q-9.5 0.5 -9.5 -9.5z"/>
      </g>
      <!-- envelope -->
      <g transform="translate(262,213)">
        <rect class="icon" x="-5" y="-3.5" width="10" height="7"/>
        <path class="icon" d="M-5 -3.5 l5 4 5 -4"/>
      </g>
      <!-- globe -->
      <g transform="translate(262,231)">
        <circle class="icon" cx="0" cy="0" r="5"/>
        <path class="icon" d="M-5 0 h10 M0 -5 v10"/>
      </g>
      <!-- home -->
      <g transform="translate(262,249)">
        <path class="icon" d="M-5 0 l5 -5 5 5 M-3.5 -1 v5.5 h7 v-5.5"/>
      </g>
    </svg>
    <div class="firm-name">Calloway<br>Immigration Law</div>
    <div class="contact">
      <div><span class="contact__name">John Smith</span><span class="contact__role">, CEO</span></div>
      <div>123 456 789</div>
      <div>name@email.com</div>
      <div>www.website.com</div>
      <div>Address Line 1</div>
      <div>Address Line 2</div>
    </div>
  </section>

  <section class="card card--front" aria-label="Card front">
    <svg class="card__bands" viewBox="0 0 525 300" aria-hidden="true">
      <polyline points="200,0 200,92 150,132 150,300" fill="none" stroke="var(--navy)" stroke-width="16"/>
      <polyline points="395,0 395,168 345,208 345,300" fill="none" stroke="var(--sky)" stroke-width="16"/>
    </svg>
    <div class="firm-name">Calloway<br>Immigration Law</div>
  </section>

</body>
</html>
```